Redesign Website for Tandara Flame

I have an existing website on https://www.tandaraflame-example.com.au/ and would like to have this redesigned professionally with new content (please refer to word document). We are fire protection engineers providing fire services design expertise and engineering design to a range of different clients.

We also provide drafting services to clients in the form of completing final commissioning documentation such as 'as-installed' drawings and fire services block plans to ensure compliance with the building code and relevant Australian Standards.

Target Market(s)

Builders, Architects, Consultants, Project Managers

Industry/Entity Type

Engineering Consultant

Coding

Coded - Design and coding required

Number of Pages Required

4 page

Font styles to use
Sans Serif

Requirements
Must have
• Home and about Page, fire services design page, fire block plans page, contact us page (4 Pages).

The website colour choice must match or compliment the new company logo.
Nice to have
• Quality photos of fire services installations in buildings to Australian Standards.

A website similar to this would be ideal http://corbellpyro-example.com.au
Should not have
• Stolen licensed photos

```html
<!DOCTYPE html>
<html lang="en">
<head>
<meta charset="utf-8">
<title>Tandara Flame – Fire Services Drawings and Block Plans</title>
<link rel="stylesheet" href="https://fonts.googleapis.com/css2?family=Quicksand:wght@500;700&family=Roboto:wght@300;400&family=Raleway:wght@400;500&display=swap">
<style>
:root{
  --orange:#f0931e;
  --orange-dark:#e5841a;
  --ink:#222;
  --grey-line:#bdbdbd;
  --panel:#f5f5f5;
  --white:#fff;
  --hero-dark:#3c3836;
  --footer-dark:#262626;
}
*{box-sizing:border-box;margin:0;padding:0}
html,body{width:1200px;height:2487px;overflow:hidden;background:var(--white)}
body{position:relative;font-family:"Raleway",sans-serif;color:var(--ink)}
.abs{position:absolute}
/* hero */
.hero-photo{left:0;top:0;width:1200px;height:700px;
  background:radial-gradient(ellipse at 30% 40%,#6a4f48 0%,#4a3f3c 40%,#2f2c2b 100%)}
.hero-band{left:0;top:630px;width:1200px;height:180px;
  background:linear-gradient(#f0931e 0%,#f0931e 25%,#f6b45a 55%,#fde7cc 80%,#fff 100%)}
.nav{left:355px;top:31px;width:510px;height:40px}
.nav a{position:absolute;font-family:"Quicksand",sans-serif;font-weight:700;font-size:14px;color:#111;text-decoration:none;line-height:1}
.nav small{display:block;font-size:7px;color:var(--orange);font-weight:500;margin-bottom:1px}
.brand-dot{left:578px;top:22px;width:44px;height:44px;border-radius:50%;background:var(--orange)}
.brand-name{left:0;width:1200px;top:88px;text-align:center;font-family:"Quicksand",sans-serif;font-weight:700;font-size:26px;color:var(--orange);letter-spacing:.5px}
.hero-title{left:0;width:1200px;top:172px;text-align:center;font-family:"Quicksand",sans-serif;font-weight:700;font-size:36px;line-height:44px;color:var(--orange)}
.hero-text{left:280px;width:640px;top:278px;text-align:center;font-family:"Roboto",sans-serif;font-weight:300;font-size:21px;line-height:28.5px;color:var(--white);text-shadow:0 1px 3px rgba(0,0,0,.6)}
.btn-outline{left:530px;top:411px;width:145px;height:30px;border:2px solid var(--white);color:var(--orange);background:rgba(255,255,255,.9);font-family:"Quicksand",sans-serif;font-weight:700;font-size:17px;letter-spacing:2px;text-align:center;line-height:26px}
.dots{left:521px;top:880px;display:flex;gap:5.5px}
.dots span{width:12px;height:12px;border-radius:50%;border:1px solid #888;background:#fff}
.dots span.on{background:#888}
/* section headings */
.sec-title{left:0;width:1200px;text-align:center;font-family:"Quicksand",sans-serif;font-weight:700;font-size:28px;color:var(--orange)}
.divider{left:540px;width:120px;height:20px}
.intro{left:195px;width:810px;top:1014px;text-align:center;font-size:11.5px;line-height:15px;color:#222}
.feature h3{font-family:"Quicksand",sans-serif;font-weight:700;font-size:16px;color:var(--orange)}
.feature p{font-size:11.5px;line-height:15px;color:#222;margin-top:6px}
.icon-ring{width:34px;height:34px;border-radius:50%;border:1.5px solid #c8c8c8;background:#fff}
/* portfolio */
.portfolio{left:0;top:1477px;width:1200px;height:670px;background:var(--panel)}
.shot{background:linear-gradient(135deg,#8c8f93,#c9cdd1 60%,#6d6f72)}
.btn-solid{background:var(--orange);color:#fff;font-family:"Quicksand",sans-serif;font-weight:700;letter-spacing:2px;text-align:center}
/* footer */
.footer{left:0;top:2147px;width:1200px;height:340px;background:linear-gradient(135deg,#3a3a3a,#1f1f1f 60%,#2c2a24)}
.foot-name{left:218px;top:2285px;font-family:"Quicksand",sans-serif;font-weight:700;font-size:22px;color:var(--orange)}
.foot-contact{left:219px;top:2333px;font-family:"Roboto",sans-serif;font-size:12px;line-height:22px;color:#fff}
.foot-contact b{color:var(--orange);font-weight:400}
.foot-nav{left:448px;top:2281px}
.foot-nav a{display:block;font-family:"Quicksand",sans-serif;font-weight:700;font-size:14px;color:#fff;text-decoration:none;margin-bottom:8px;line-height:15px}
.foot-nav small{display:block;font-size:8px;font-weight:500;line-height:9px}
.form{left:562px;top:2218px;width:444px;height:200px;background:rgba(245,245,245,.93)}
.form h4{position:absolute;left:0;width:444px;top:14px;text-align:center;font-family:"Quicksand",sans-serif;font-weight:700;font-size:16px;color:var(--orange)}
.field{position:absolute;height:19px;border:1px solid #d0d0d0;background:#f0f0f0;font-family:"Roboto",sans-serif;font-size:9px;color:#555;padding:3px 5px}
</style>
</head>
<body>

<!-- Hero -->
<div class="abs hero-photo" role="img" aria-label="Photo of a fire pump room with red valves and pipework"></div>
<div class="abs hero-band" role="img" aria-label="Orange band with flame pattern fading to white"></div>

<svg class="abs" style="left:355px;top:31px" width="510" height="40" viewBox="0 0 510 40">
  <polygon points="12,0 498,0 510,20 498,40 12,40 0,20" fill="#fff"/>
</svg>
<nav class="abs nav">
  <a style="left:38px;top:14px">HOME</a>
  <a style="left:110px;top:14px">ABOUT US</a>
  <a style="left:290px;top:9px"><small>FIRE</small>SERVICES</a>
  <a style="left:368px;top:9px"><small>FIRE BLOCK</small>PLANS</a>
  <a style="left:425px;top:18px">CONTACT</a>
</nav>
<div class="abs brand-dot"></div>
<div class="abs brand-name">TANDARA FLAME</div>

<h1 class="abs hero-title">FIRE SERVICES<br>DRAWINGS AND BLOCK PLANS</h1>
<p class="abs hero-text">We pride ourselves in our ability to meet the demand of our clients and our ability to consistently uphold our 3 key business values in providing our services at quick turnaround, quality service at competitive pricing</p>
<div class="abs btn-outline">LEARN MORE</div>

<svg class="abs" style="left:318px;top:487px" width="542" height="384" viewBox="0 0 542 384">
  <polygon points="105,2 437,2 540,192 437,382 105,382 2,192" fill="#f3f3f1" stroke="#f0931e" stroke-width="4"/>
  <rect x="60" y="60" width="0" height="0" role="img" aria-label="Fire services block plan drawing showing zones and flow switches"/>
</svg>
<div class="abs dots"><span></span><span></span><span></span><span></span><span></span><span></span><span></span><span class="on"></span></div>

<!-- Values -->
<h2 class="abs sec-title" style="top:950px">LOREM IPSUM</h2>
<svg class="abs divider" style="top:989px" viewBox="0 0 120 20">
  <g stroke="#f0931e" stroke-width="1"><line x1="0" y1="10" x2="50" y2="10"/><line x1="25" y1="7" x2="50" y2="7"/><line x1="70" y1="10" x2="120" y2="10"/><line x1="70" y1="7" x2="95" y2="7"/></g>
  <circle cx="60" cy="9" r="4" fill="#f0931e"/>
</svg>
<p class="abs intro">Aliquip ex ea commodo consequat. Duis autem vel eum iriure dolor in hendrerit in vulputate velit esse molestie consequat, vel illum dolore eu feugiat nulla facilisis at vero eros et accumsan et iusto odio dignissim qui blandit praesent luptatum zzril delenit augue duis dolore te feugait nulla facilisi.</p>

<svg class="abs" style="left:190px;top:1080px" width="830" height="300" viewBox="0 0 830 300">
  <g fill="none" stroke="#bdbdbd" stroke-width="1.2">
    <polyline points="40,18 310,18 365,66"/>
    <polyline points="40,270 310,270 365,222"/>
    <line x1="495" y1="142" x2="800" y2="142"/>
    <circle cx="410" cy="142" r="84"/>
  </g>
  <circle cx="410" cy="142" r="74" fill="#f0931e"/>
</svg>
<div class="abs icon-ring" style="left:194px;top:1081px"></div>
<svg class="abs" style="left:202px;top:1089px" width="18" height="18" viewBox="0 0 18 18"><circle cx="9" cy="9" r="7" fill="none" stroke="#f0931e" stroke-width="1.4"/><polyline points="5,9 8,12 15,4" fill="none" stroke="#f0931e" stroke-width="1.6"/></svg>
<div class="abs icon-ring" style="left:971px;top:1205px"></div>
<svg class="abs" style="left:979px;top:1213px" width="18" height="18" viewBox="0 0 18 18"><path d="M3 3h8l4 4-6 6-6-6z" fill="none" stroke="#f0931e" stroke-width="1.4"/><circle cx="7" cy="7" r="1.4" fill="#f0931e"/></svg>
<div class="abs icon-ring" style="left:194px;top:1333px"></div>
<svg class="abs" style="left:202px;top:1341px" width="18" height="18" viewBox="0 0 18 18"><path d="M4 14l1-4 8-8 3 3-8 8z M3 16h12" fill="none" stroke="#f0931e" stroke-width="1.4"/></svg>

<div class="abs feature" style="left:236px;top:1075px;width:250px">
  <h3>LOREM IPSUM</h3>
  <p>We pride ourselves on our prompt service and delivery of all of our projects. You can rely on us to meet your project deadlines!</p>
</div>
<div class="abs feature" style="left:730px;top:1199px;width:235px;text-align:right">
  <h3>LOREM IPSUM</h3>
  <p>We strive to always be competitively priced are very competitively priced.</p>
</div>
<div class="abs feature" style="left:236px;top:1327px;width:240px">
  <h3>LOREM IPSUM</h3>
  <p>Our customer service and our output is guaranteed to be of the highest quality. You will not be disappointed.</p>
</div>

<!-- Portfolio -->
<section class="abs portfolio"></section>
<h2 class="abs sec-title" style="top:1545px">PORTFOLIO</h2>
<svg class="abs divider" style="top:1584px" viewBox="0 0 120 20">
  <g stroke="#f0931e" stroke-width="1"><line x1="0" y1="10" x2="50" y2="10"/><line x1="25" y1="7" x2="50" y2="7"/><line x1="70" y1="10" x2="120" y2="10"/><line x1="70" y1="7" x2="95" y2="7"/></g>
  <circle cx="60" cy="9" r="4" fill="#f0931e"/>
</svg>
<div class="abs shot" style="left:194px;top:1624px;width:199px;height:112px" role="img" aria-label="Industrial plant room with ductwork"></div>
<div class="abs shot" style="left:194px;top:1752px;width:199px;height:112px" role="img" aria-label="Factory floor with sprinkler pipework"></div>
<div class="abs shot" style="left:194px;top:1880px;width:199px;height:149px" role="img" aria-label="Industrial building exterior with hydrant"></div>
<div class="abs shot" style="left:410px;top:1624px;width:596px;height:405px;background:linear-gradient(#b9bcbf,#8d8f8f 55%,#a7a39a)" role="img" aria-label="Underground car park with red sprinkler pipes and yellow columns"></div>
<div class="abs btn-solid" style="left:533px;top:2048px;width:134px;height:25px;line-height:25px;font-size:15px">VIEW ALL</div>

<!-- Footer -->
<footer class="abs footer" role="img" aria-label="Dark car park photo background"></footer>
<div class="abs" style="left:280px;top:2222px;width:52px;height:52px;border-radius:50%;background:var(--orange)"></div>
<div class="abs foot-name">TANDARA FLAME</div>
<div class="abs foot-contact">
  <div><b>ABN:</b> 00 000 000 000</div>
  <div><b>M:</b> +61 400 000 000</div>
  <div><b>E:</b> info@tandaraflame-example.com.au</div>
  <div><b>W:</b> www.tandaraflame-example.com.au</div>
</div>
<nav class="abs foot-nav">
  <a style="margin-top:0">HOME</a>
  <a>ABOUT US</a>
  <a><small>FIRE</small>SERVICES</a>
  <a><small>FIRE BLOCK</small>PLANS</a>
  <a style="margin-top:6px">CONTACT</a>
</nav>
<form class="abs form">
  <h4>KEEP IN TOUCH WITH US</h4>
  <svg style="position:absolute;left:192px;top:36px" width="60" height="12" viewBox="0 0 60 12"><g stroke="#f0931e" stroke-width="1"><line x1="0" y1="6" x2="25" y2="6"/><line x1="35" y1="6" x2="60" y2="6"/></g><circle cx="30" cy="6" r="3" fill="#f0931e"/></svg>
  <div class="field" style="left:16px;top:50px;width:130px">Name:</div>
  <div class="field" style="left:157px;top:50px;width:130px">Phone:</div>
  <div class="field" style="left:298px;top:50px;width:130px">Email:</div>
  <div class="field" style="left:16px;top:81px;width:412px;height:68px">Message:</div>
  <div class="btn-solid" style="position:absolute;left:164px;top:164px;width:116px;height:21px;line-height:21px;font-size:12px">SUBMIT NOW</div>
</form>

</body>
</html>
```